Business Card and Stationery for Chiropractic Clinic
Marlowe Spine Studio, LLC
Business Card and Stationery for Chiropractic Clinic - Health
Creative Brief
Simple
Dorothea R. Halvik, DC
Chiropractor / Owner
2718 East Pellham Street Franklin, WI 53187
dorahalvik@mailnest.example
www.marlowespinestudio.example
Appointments For___________________ Date:__________, Time: ___________ The greatest compliment we can receive is a referral.

```html
<!DOCTYPE html>
<html lang="en">
<head>
<meta charset="utf-8">
<title>Marlowe Spine Studio, LLC — Business Card</title>
<link rel="stylesheet" href="https://fonts.googleapis.com/css2?family=Cinzel:wght@400;600;700&display=swap">
<style>
  :root {
    --page-bg: #e9e6e2;
    --card-white: #ffffff;
    --brand-red: #a3252b;
    --band-red: #9e2a2f;
    --band-edge: #c9c9c9;
    --band-edge-dark: #8a8a8a;
    --ink-light: #ffffff;
    --ink-soft: #f1dcdc;
    --shadow: rgba(0, 0, 0, 0.18);
  }
  * { box-sizing: border-box; margin: 0; padding: 0; }
  html, body {
    width: 1200px;
    height: 900px;
    overflow: hidden;
    background: var(--page-bg);
  }
  .stage {
    width: 1200px;
    height: 900px;
    display: flex;
    align-items: center;
    justify-content: center;
  }
  .business-card {
    position: relative;
    width: 1050px;
    height: 600px;
    background: var(--card-white);
    box-shadow: 0 14px 40px var(--shadow);
    font-family: "Cinzel", serif;
    overflow: hidden;
  }
  .brand {
    position: absolute;
    left: 58px;
    top: 50px;
    display: flex;
    align-items: center;
    gap: 26px;
  }
  .brand-mark {
    width: 128px;
    height: 128px;
    border-radius: 50%;
    background: var(--brand-red);
    flex: none;
  }
  .brand-name {
    color: var(--brand-red);
    font-weight: 700;
    line-height: 1.02;
    text-transform: uppercase;
  }
  .brand-name .line-main {
    display: block;
    font-size: 50px;
    letter-spacing: 1px;
  }
  .brand-name .line-sub {
    display: block;
    font-size: 32px;
    letter-spacing: 4px;
    margin-top: 6px;
  }
  .info-band {
    position: absolute;
    left: 0;
    right: 0;
    top: 240px;
    height: 256px;
    background: var(--band-red);
    border-top: 6px solid var(--band-edge);
    border-bottom: 6px solid var(--band-edge);
    box-shadow: 0 -1px 0 var(--band-edge-dark), 0 1px 0 var(--band-edge-dark);
    display: flex;
    justify-content: space-between;
    align-items: flex-start;
    padding: 40px 54px 0 40px;
    color: var(--ink-light);
  }
  .contact-list {
    list-style: none;
    font-size: 17px;
    letter-spacing: 0.6px;
    line-height: 1.5;
  }
  .contact-list li {
    display: flex;
    align-items: center;
    gap: 10px;
  }
  .contact-list li.continued { padding-left: 32px; }
  .contact-icon {
    width: 22px;
    height: 22px;
    flex: none;
  }
  .practitioner {
    text-align: right;
    padding-top: 16px;
  }
  .practitioner-name {
    font-size: 24px;
    letter-spacing: 0.8px;
    font-weight: 400;
  }
  .practitioner-title {
    font-size: 17px;
    letter-spacing: 0.8px;
    color: var(--ink-soft);
    margin-top: 4px;
  }
</style>
</head>
<body>
<main class="stage">
  <article class="business-card">
    <header class="brand">
      <span class="brand-mark" aria-hidden="true"></span>
      <h1 class="brand-name">
        <span class="line-main">Marlowe Spine</span>
        <span class="line-sub">Studio, LLC</span>
      </h1>
    </header>

    <section class="info-band">
      <ul class="contact-list">
        <li>
          <svg class="contact-icon" viewBox="0 0 24 24" aria-hidden="true">
            <circle cx="12" cy="12" r="11" fill="#fff"/>
            <path d="M12 5.5a4 4 0 0 0-4 4c0 3 4 8 4 8s4-5 4-8a4 4 0 0 0-4-4zm0 5.5a1.5 1.5 0 1 1 0-3 1.5 1.5 0 0 1 0 3z" fill="var(--band-red)"/>
          </svg>
          2718 East Pellham Street
        </li>
        <li class="continued">Franklin, WI 53187</li>
        <li>
          <svg class="contact-icon" viewBox="0 0 24 24" aria-hidden="true">
            <circle cx="12" cy="12" r="11" fill="#fff"/>
            <path d="M8.6 6.5l1.8-.4 1.2 2.8-1.3 1a7 7 0 0 0 3.8 3.8l1-1.3 2.8 1.2-.4 1.8c-.2.6-.7.9-1.3.9A9.5 9.5 0 0 1 7.7 7.8c0-.6.3-1.1.9-1.3z" fill="var(--band-red)"/>
          </svg>
          (262) 418-3096
        </li>
        <li>
          <svg class="contact-icon" viewBox="0 0 24 24" aria-hidden="true">
            <circle cx="12" cy="12" r="11" fill="#fff"/>
            <rect x="8" y="5" width="8" height="14" rx="1.5" fill="var(--band-red)"/>
            <rect x="9.3" y="6.8" width="5.4" height="9" fill="#fff"/>
          </svg>
          (262) 730-5148
        </li>
        <li>
          <svg class="contact-icon" viewBox="0 0 24 24" aria-hidden="true">
            <circle cx="12" cy="12" r="11" fill="#fff"/>
            <rect x="6" y="8" width="12" height="8.5" rx="1" fill="var(--band-red)"/>
            <path d="M6.5 8.6l5.5 4.2 5.5-4.2" stroke="#fff" stroke-width="1.2" fill="none"/>
          </svg>
          dorahalvik@mailnest.example
        </li>
        <li>
          <svg class="contact-icon" viewBox="0 0 24 24" aria-hidden="true">
            <circle cx="12" cy="12" r="11" fill="#fff"/>
            <circle cx="12" cy="12" r="6" stroke="var(--band-red)" stroke-width="1.4" fill="none"/>
            <ellipse cx="12" cy="12" rx="2.6" ry="6" stroke="var(--band-red)" stroke-width="1.2" fill="none"/>
            <path d="M6 12h12" stroke="var(--band-red)" stroke-width="1.2"/>
          </svg>
          www.marlowespinestudio.example
        </li>
      </ul>

      <div class="practitioner">
        <p class="practitioner-name">Dorothea R. Halvik, DC</p>
        <p class="practitioner-title">Chiropractor / Owner</p>
      </div>
    </section>
  </article>
</main>
</body>
</html>
```